Business card design only (Have Logo Online) Shoudl be quick and easy for designer

We would like to have a business card design that is in-line with our company logo. Final deliverables should include two EPS extension file. One for the front card design and the other the back-end design. Please also indicate the font style used.

Advisory Pebble is a social enterprise that focuses on utilizing technology, unique methodologies and international partnerships to provide a one-stop location for economical and dependable IT-related solutions.

Target Market(s)

Micro, small and medium business owners.

Industry/Entity Type

Business

Requirements
Must have
• The business card should incorporate our company logo.
Nice to have
• A little web 2.0 style would be nice but I haven''t decided yet.

```html
<!DOCTYPE html>
<html lang="en">
<head>
<meta charset="utf-8">
<title>Advisory Pebble – Business Card</title>
<link rel="stylesheet" href="https://fonts.googleapis.com/css2?family=Noto+Serif:wght@400;700&family=Michroma&display=swap">
<style>
  :root {
    --stage: #d6d6d6;
    --card-white: #ffffff;
    --lime: #b8fd7e;
    --leaf: #44b72c;
    --ink: #111111;
    --forest: #256632;
    --moss: #5a9d4e;
    --forest-text: #1d4a26;
    --paper-white: #f4f8f4;
  }
  * { margin: 0; padding: 0; box-sizing: border-box; }
  html, body { width: 1120px; height: 1200px; overflow: hidden; }
  body {
    background: var(--stage);
    position: relative;
    font-family: "Noto Serif", Georgia, serif;
  }
  .card {
    position: absolute;
    width: 663px;
    height: 376px;
    overflow: hidden;
  }
  .card-front {
    left: 110px; top: 156px;
    background: var(--card-white);
    border: 1px solid #555;
  }
  .card-back {
    left: 347px; top: 602px;
    background: var(--forest);
  }
  .card-art { position: absolute; inset: 0; }

  .brand-name {
    position: absolute;
    left: 68px; top: 114px;
    font-size: 27px;
    font-weight: 700;
    color: var(--leaf);
    white-space: nowrap;
  }
  .address {
    position: absolute;
    right: 29px; top: 22px;
    text-align: right;
    color: var(--leaf);
    font-size: 21px;
    line-height: 25px;
  }
  .person-name {
    position: absolute;
    left: 38px; top: 210px;
    font-size: 28px;
    font-weight: 700;
    color: var(--leaf);
    letter-spacing: 0.5px;
  }
  .person-role {
    position: absolute;
    left: 38px; top: 246px;
    font-size: 20px;
    color: var(--ink);
  }
  .contact {
    position: absolute;
    left: 38px; top: 290px;
    font-size: 22px;
    line-height: 28px;
    color: var(--ink);
  }
  .contact .domain { font-weight: 700; }

  .tagline {
    position: absolute;
    left: 34px; top: 218px;
    font-size: 20px;
    font-weight: 700;
    line-height: 24px;
    color: var(--forest-text);
  }
  .web-address {
    position: absolute;
    left: 34px; top: 324px;
    font-family: "Michroma", Arial, sans-serif;
    font-size: 16px;
    letter-spacing: 2px;
    color: var(--paper-white);
  }
</style>
</head>
<body>
  <section class="card card-front" aria-label="Front of business card">
    <svg class="card-art" viewBox="0 0 663 376" aria-hidden="true">
      <circle class="brand-dot" cx="118" cy="98" r="87" fill="var(--lime)"/>
      <path class="corner-swoosh" d="M593 0 L663 0 L663 376 L435 376 C560 330 625 230 617 115 C614 70 605 35 593 0 Z" fill="var(--lime)"/>
    </svg>
    <div class="brand-name">Advisory Pebble</div>
    <div class="address">4120 Alder Lane<br>BC Canada<br>V6K 2P3</div>
    <h1 class="person-name">MARLEN OSKAR</h1>
    <p class="person-role">Founder</p>
    <p class="contact">1-604-555-0148<br>marlen.oskar@<span class="domain">advisorypebble.com</span></p>
  </section>

  <section class="card card-back" aria-label="Back of business card">
    <svg class="card-art" viewBox="0 0 663 376" aria-hidden="true">
      <circle class="back-disc" cx="507" cy="182" r="235" fill="var(--moss)"/>
    </svg>
    <p class="tagline">Your one-stop location<br>for economical and<br>dependable IT-related solutions</p>
    <p class="web-address">ADVISORYPEBBLE.COM</p>
  </section>
</body>
</html>
```